Natural Skincare brand needs new labels!

We are a natural and organic skin care brand based in the united states. We are looking for unique product label designs that will help our brand stand out. We want the labels to look elegant and natural, but also incorporate some color. We want a design aspect like a line drawing on the labels, see examples. Please refer to our website to see our current labels and to get more of a feel of who we are. Our logo is included. We are looking for 5 labels for 5 different Products.
1. Body butter: 1.5"x9" rectangle wrap around 12oz jar with black lid
2. Eczema Salve: 1.5" circle silver metal tin
3. Glow Serum: 1.5"x3" rectangle Blue Dropper Bottle with black top
4. Mineral Mist: 1.5"x3" clear glass sprayer bottle (want clear label)
website: www.velmirabotanics.com
Instagram: @velmirabotanics

```html
<!DOCTYPE html>
<html lang="en">
<head>
<meta charset="UTF-8">
<title>Velmira Skin — Product Labels</title>
<link href="https://fonts.googleapis.com/css2?family=Josefin+Sans:wght@400;600&display=swap" rel="stylesheet">
<style>
  :root {
    --board-light: #f4f4f4;
    --board-dark: #c9c9c9;
    --ink-black: #0c0c0c;
    --label-white: #ffffff;
    --brand-coral: #ef7f6d;
    --band-green: #08704a;
    --band-text: #ffffff;
    --sketch-grey: #e6e6e6;
  }
  * { box-sizing: border-box; margin: 0; padding: 0; }
  html, body { width: 1200px; height: 848px; overflow: hidden; }
  body {
    position: relative;
    font-family: "Josefin Sans", sans-serif;
    background: radial-gradient(ellipse at 50% 40%, var(--board-light) 0%, #e4e4e4 55%, var(--board-dark) 100%);
  }
  .corner-ribbon {
    position: absolute; left: -60px; top: 30px;
    width: 300px; height: 26px; background: var(--ink-black);
    transform: rotate(-30deg); transform-origin: left top;
  }
  .caption-bar {
    position: absolute; left: 0; bottom: 0; width: 1200px; height: 56px;
    background: var(--ink-black);
  }
  .caption-bar p {
    position: absolute; left: 62px; top: 20px;
    color: #fff; font-size: 14px; letter-spacing: 0.2px;
  }
  .label {
    position: absolute; width: 536px; height: 268px;
    background: var(--label-white); overflow: hidden;
  }
  .label--butter { left: 90px; top: 115px; }
  .label--serum { left: 172px; top: 372px; }
  .label--mist { left: 570px; top: 475px; }
  .waves { position: absolute; inset: 0; width: 100%; height: 100%; }
  .illustration {
    position: absolute; border-radius: 4px;
    background: linear-gradient(160deg, #f3f3f3, var(--sketch-grey));
    opacity: 0.85;
  }
  .label--butter .illustration { left: 10px; top: 95px; width: 140px; height: 130px; }
  .label--serum .illustration { left: 20px; top: 33px; width: 110px; height: 190px; }
  .label--mist .illustration { left: 10px; top: 35px; width: 145px; height: 190px; }
  .brand {
    position: absolute; display: flex; align-items: center; gap: 8px;
    color: var(--brand-coral); font-weight: 600; font-size: 28px;
    line-height: 1; white-space: nowrap;
  }
  .brand__dot {
    width: 20px; height: 20px; border-radius: 50%; background: var(--brand-coral); flex: none;
  }
  .label--butter .brand { left: 165px; top: 86px; }
  .label--serum .brand { left: 162px; top: 92px; }
  .label--mist .brand { left: 168px; top: 92px; }
  .product-band {
    position: absolute; left: 0; bottom: 0; width: 100%; height: 37px;
    background: var(--band-green);
    display: flex; align-items: center; justify-content: center;
  }
  .product-name {
    color: var(--band-text); font-size: 11px; font-weight: 600;
    letter-spacing: 6px; text-transform: uppercase;
  }
  .tin {
    position: absolute; left: 738px; top: 138px; width: 267px; height: 267px;
    background: var(--label-white);
  }
  .tin__face {
    position: absolute; left: 6px; top: 4px; width: 256px; height: 256px;
    border-radius: 50%; overflow: hidden; background: var(--label-white);
  }
  .tin .brand { left: 32px; top: 106px; font-size: 25px; }
  .tin .brand__dot { width: 18px; height: 18px; }
  .tin .product-band { height: 56px; align-items: flex-start; padding-top: 12px; }
</style>
</head>
<body>
  <div class="corner-ribbon"></div>

  <section class="label label--butter">
    <svg class="waves" viewBox="0 0 536 268" preserveAspectRatio="none" aria-hidden="true">
      <path d="M0 0H536V60C420 20 300 80 180 60C110 48 50 40 0 55Z" fill="#fbc36b" opacity="0.75"/>
      <path d="M0 30C120 10 220 60 330 40C420 25 480 0 536 10V220C470 180 420 120 340 110C240 95 120 70 0 65Z" fill="#f2a58a" opacity="0.45"/>
      <path d="M260 90C360 60 450 40 536 70V230C460 200 380 150 260 90Z" fill="#e9a2a8" opacity="0.45"/>
    </svg>
    <div class="illustration" role="img" aria-label="Line drawing of a block of butter with curls and a knife"></div>
    <div class="brand"><span class="brand__dot"></span>Velmira Skin</div>
    <div class="product-band"><span class="product-name">Body Butter</span></div>
  </section>

  <section class="tin">
    <div class="tin__face">
      <svg class="waves" viewBox="0 0 256 256" preserveAspectRatio="none" aria-hidden="true">
        <path d="M0 0H256V70C190 50 120 80 60 95C35 100 15 100 0 98Z" fill="#f8df6a" opacity="0.8"/>
        <path d="M0 95C70 80 150 60 256 80V170C200 140 120 120 0 120Z" fill="#f5b77a" opacity="0.6"/>
        <path d="M120 110C180 100 220 110 256 130V200C210 170 170 140 120 110Z" fill="#e9a2a8" opacity="0.5"/>
      </svg>
      <div class="brand"><span class="brand__dot"></span>Velmira Skin</div>
      <div class="product-band"><span class="product-name">Eczema Salve</span></div>
    </div>
  </section>

  <section class="label label--serum">
    <svg class="waves" viewBox="0 0 536 268" preserveAspectRatio="none" aria-hidden="true">
      <path d="M0 0H536V30C420 10 300 50 160 45C90 42 40 40 0 48Z" fill="#b9c4f2" opacity="0.7"/>
      <path d="M0 40C140 20 260 60 380 40C450 30 500 20 536 25V160C460 120 380 90 260 85C160 80 80 70 0 75Z" fill="#bfe9dd" opacity="0.5"/>
    </svg>
    <div class="illustration" role="img" aria-label="Line drawing of a dropper bottle"></div>
    <div class="brand"><span class="brand__dot"></span>Velmira Skin</div>
    <div class="product-band"><span class="product-name">Glow Serum</span></div>
  </section>

  <section class="label label--mist">
    <svg class="waves" viewBox="0 0 536 268" preserveAspectRatio="none" aria-hidden="true">
      <path d="M0 0H536V40C420 20 300 55 170 45C100 40 40 35 0 40Z" fill="#a9e6ee" opacity="0.7"/>
      <path d="M0 35C140 20 260 60 390 45C460 35 510 30 536 35V180C460 140 380 110 260 95C160 85 80 65 0 70Z" fill="#c6ecd8" opacity="0.55"/>
    </svg>
    <div class="illustration" role="img" aria-label="Line drawing of a quartz crystal cluster"></div>
    <div class="brand"><span class="brand__dot"></span>Velmira Skin</div>
    <div class="product-band"><span class="product-name">Mineral Mist</span></div>
  </section>

  <footer class="caption-bar"><p>Natural Skincare brand new labels</p></footer>
</body>
</html>
```